buseisness card

design a card that similar to my web site
BRIXENTAPLORLLC .COM

Contact Information for Business Card

NAME PHONE # WEBSITE EMAIL AND DISCTIPTION OF WHAT WE DO

Colors
0054AA
0677BA
7BADD7
CADEEF
E8F1F8

Requirements
Must have
• lOGO AND DETAILS
Nice to have
• I LIKE THE WATER LIKE ON MY WEB SITE

```html
<!DOCTYPE html>
<html lang="en">
<head>
<meta charset="utf-8">
<title>Brixen Taplor – Business Card</title>
<link href="https://fonts.googleapis.com/css2?family=Montserrat:wght@600;700&family=Roboto:ital,wght@0,400;0,700;1,400&display=swap" rel="stylesheet">
<style>
  :root{
    --deep:#0054AA;
    --ocean:#0677BA;
    --sky:#7BADD7;
    --mist:#CADEEF;
    --foam:#E8F1F8;
    --brand:#2a8ec0;
    --aqua:#5fcde8;
    --paper:#ffffff;
    --backdrop:#e9edf1;
  }
  *{box-sizing:border-box;margin:0;padding:0}
  html,body{width:1200px;height:900px;overflow:hidden;background:var(--backdrop)}
  .sheet{width:1200px;height:900px;display:flex;flex-direction:column;align-items:center;justify-content:center;gap:56px}
  .card{position:relative;width:620px;height:354px;border-radius:22px;background:var(--paper);overflow:hidden;box-shadow:0 10px 30px rgba(0,40,90,.18)}
  .wordmark{display:flex;align-items:center;gap:14px;font-family:"Montserrat",sans-serif;font-weight:700;color:var(--brand);letter-spacing:.06em;white-space:nowrap}
  .wordmark__dot{border-radius:50%;background:var(--brand)}
  .card--front{display:flex;align-items:center;justify-content:center}
  .card--front .wordmark{font-size:40px}
  .card--front .wordmark__dot{width:38px;height:38px}
  .card__water{position:absolute;inset:0;width:100%;height:100%}
  .card--back .wordmark{position:absolute;top:70px;left:236px;font-size:25px}
  .card--back .wordmark__dot{width:22px;height:22px}
  .person{position:absolute;left:40px;top:206px;color:#fff;font-family:"Roboto",sans-serif;text-align:right;width:230px}
  .person__name{font-weight:700;font-size:24px;letter-spacing:.01em}
  .person__role{font-style:italic;font-size:14px;margin-top:4px}
  .divider{position:absolute;left:292px;top:204px;width:1px;height:70px;background:rgba(255,255,255,.75)}
  .contacts{position:absolute;left:312px;top:208px;list-style:none;color:#fff;font-family:"Roboto",sans-serif;font-size:14px;line-height:21px}
  .contacts li{display:flex;align-items:center;gap:8px}
  .contacts svg{width:12px;height:12px;flex:none}
  .address{position:absolute;left:40px;bottom:26px;color:#fff;font-family:"Roboto",sans-serif;font-size:14px;letter-spacing:.01em}
</style>
</head>
<body>
<main class="sheet">
  <section class="card card--front" aria-label="Card front">
    <div class="wordmark"><span class="wordmark__dot"></span>BRIXEN TAPLOR</div>
  </section>

  <section class="card card--back" aria-label="Card back">
    <svg class="card__water" viewBox="0 0 620 354" preserveAspectRatio="none">
      <defs>
        <linearGradient id="sea" x1="0" y1="0" x2="0" y2="1">
          <stop offset="0" stop-color="#6fd0ea"/>
          <stop offset=".45" stop-color="#1a8ccc"/>
          <stop offset="1" stop-color="#0b4fae"/>
        </linearGradient>
        <linearGradient id="crest" x1="0" y1="0" x2="1" y2="0">
          <stop offset="0" stop-color="#bfeaf6"/>
          <stop offset="1" stop-color="#7fd6ee"/>
        </linearGradient>
      </defs>
      <path d="M0,96 C160,100 330,150 470,176 C540,189 590,192 620,190 L620,354 L0,354 Z" fill="url(#crest)" opacity=".7"/>
      <path d="M0,110 C170,118 330,168 470,192 C540,204 590,206 620,204 L620,354 L0,354 Z" fill="url(#sea)"/>
      <path d="M0,104 C170,110 330,160 470,185 C545,198 595,199 620,197" fill="none" stroke="#e6f8fd" stroke-width="2" opacity=".8"/>
      <path d="M0,126 C180,136 340,184 480,206 C545,216 595,216 620,214" fill="none" stroke="#9fe2f4" stroke-width="1.5" opacity=".6"/>
    </svg>

    <div class="wordmark"><span class="wordmark__dot"></span>BRIXEN TAPLOR</div>

    <div class="person">
      <p class="person__name">DORIAN VALE</p>
      <p class="person__role">Founder &amp; CEO</p>
    </div>
    <span class="divider"></span>
    <ul class="contacts">
      <li><svg viewBox="0 0 12 12"><path d="M3 1 L5 3.5 L4 5 C4.8 6.6 5.6 7.4 7 8 L8.5 7 L11 9 L9.5 11 C5 10.5 1.5 7 1 2.5 Z" fill="#fff"/></svg>+740 555 0182</li>
      <li><svg viewBox="0 0 12 12"><rect x="1" y="2.5" width="10" height="7" fill="#fff"/><path d="M1 2.5 L6 6.5 L11 2.5" fill="none" stroke="#1a7cc4" stroke-width="1"/></svg>hello@bt204.com</li>
      <li><svg viewBox="0 0 12 12"><g fill="none" stroke="#fff" stroke-width="1"><circle cx="6" cy="6" r="5"/><ellipse cx="6" cy="6" rx="2.2" ry="5"/><path d="M1 6 H11"/></g></svg>www.brixentaplorllc.com</li>
    </ul>
    <p class="address">1840 Harbor Crest Drive Dayton, OH 45402</p>
  </section>
</main>
</body>
</html>
```